Brightwell Docket

Conference flyer. Target audience is for attorneys and bail agents. App allows their clients to check-in, make payments and receive payments.
See website brightwelldocket.example for product
Details. Emphasize Payment button, check-ins and court reminders.

Attorneys, Bail Agents, courts, probation

Court House

• Picture of someone taking a selfie for a check-in!

```html
<!DOCTYPE html>
<html lang="en">
<head>
<meta charset="utf-8">
<title>Brightwell Docket – Conference Flyer</title>
<link href="https://fonts.googleapis.com/css2?family=Noto+Sans:ital,wght@0,400;0,700;0,800;1,800&display=swap" rel="stylesheet">
<style>
  :root {
    --navy: #1b2a55;
    --deep-blue: #0a2468;
    --bright-blue: #0057b3;
    --icon-navy: #0d2f6b;
    --white: #ffffff;
    --alert-red: #e8000f;
  }
  * { margin: 0; padding: 0; box-sizing: border-box; }
  html, body { width: 854px; height: 1200px; overflow: hidden; background: var(--navy); }
  body { font-family: "Noto Sans", sans-serif; color: var(--white); }
  .flyer { position: relative; width: 854px; height: 1200px; overflow: hidden; background: var(--navy); }
  .backdrop { position: absolute; inset: 0; }
  .headline {
    position: absolute; left: 42px; top: 34px;
    font-size: 48px; line-height: 60px; font-weight: 800; font-style: italic;
    letter-spacing: 5px; white-space: nowrap;
  }
  .feature { position: absolute; left: 26px; width: 182px; text-align: center; }
  .feature-badge {
    width: 148px; height: 148px; margin: 0 auto 14px;
    border-radius: 50%; border: 5px solid var(--white); background: var(--icon-navy);
    display: flex; align-items: center; justify-content: center;
  }
  .feature-label { font-size: 19px; font-weight: 700; line-height: 25px; letter-spacing: 2px; }
  .feature--checkins { top: 210px; }
  .feature--dates { top: 416px; }
  .feature--payments { top: 642px; }
  .brand-seal {
    position: absolute; left: 345px; top: 285px; width: 440px; height: 440px;
    border-radius: 50%; border: 14px solid var(--icon-navy);
    display: flex; align-items: center; justify-content: center; text-align: center;
  }
  .brand-name { color: var(--icon-navy); font-size: 48px; font-weight: 800; line-height: 58px; }
  .and-more {
    position: absolute; left: 36px; top: 872px;
    font-size: 50px; font-weight: 800; font-style: italic; letter-spacing: 4px; white-space: nowrap;
  }
  .cta {
    position: absolute; left: 230px; top: 972px; width: 416px; height: 78px;
    background: var(--white); border-radius: 39px;
    display: flex; align-items: center; justify-content: center;
    color: var(--alert-red); font-size: 32px; font-weight: 700; letter-spacing: 3px;
  }
  .agent-name {
    position: absolute; left: 0; width: 100%; top: 1056px; text-align: center;
    font-size: 46px; font-weight: 700; line-height: 58px; letter-spacing: 2px;
  }
  .contact { position: absolute; top: 1098px; text-align: center; white-space: nowrap; }
  .contact-label { font-size: 24px; font-weight: 400; line-height: 32px; letter-spacing: 1.5px; }
  .contact-value { font-size: 25px; font-weight: 700; line-height: 36px; letter-spacing: 2px; }
  .contact--email { left: 12px; width: 300px; }
  .contact--phone { left: 596px; width: 236px; }
</style>
</head>
<body>
<main class="flyer">
  <svg class="backdrop" width="854" height="1200" viewBox="0 0 854 1200" aria-hidden="true">
    <path d="M380 0 H854 V1200 H560 C330 1000 250 600 380 0 Z" fill="var(--deep-blue)"/>
    <path d="M460 0 C220 200 110 520 190 860 C230 1020 300 1120 380 1200 H470 C300 1000 240 620 330 330 C370 200 420 80 520 0 Z" fill="var(--bright-blue)"/>
    <path d="M852 190 C560 160 330 330 320 600 C310 850 560 1060 852 1110 Z" fill="var(--bright-blue)"/>
    <path d="M852 232 C590 200 360 360 352 600 C345 830 570 1030 852 1078 Z" fill="var(--white)"/>
  </svg>

  <h1 class="headline">THE ONLY APP YOU'LL NEED<br>FOR YOUR DAY IN COURT.</h1>

  <section class="feature feature--checkins">
    <div class="feature-badge">
      <svg width="84" height="90" viewBox="0 0 84 90" fill="none" stroke="#fff" stroke-width="4" stroke-linecap="round">
        <path d="M36 84 C18 60 8 46 8 32 A28 28 0 0 1 64 32 C64 38 62 42 60 46"/>
        <circle cx="36" cy="30" r="10"/>
        <circle cx="62" cy="66" r="16"/>
        <path d="M54 66 L60 72 L70 61"/>
      </svg>
    </div>
    <p class="feature-label">MY CHECK-INS</p>
  </section>

  <section class="feature feature--dates">
    <div class="feature-badge">
      <svg width="86" height="80" viewBox="0 0 86 80">
        <rect x="4" y="12" width="78" height="64" rx="6" fill="#fff"/>
        <rect x="20" y="2" width="5" height="18" rx="2" fill="#fff"/>
        <rect x="61" y="2" width="5" height="18" rx="2" fill="#fff"/>
        <rect x="4" y="22" width="78" height="4" fill="var(--icon-navy)"/>
        <g stroke="var(--icon-navy)" stroke-width="3" fill="none">
          <path d="M43 34 V66 M30 66 H56 M24 40 H62"/>
          <path d="M24 40 L17 54 H31 Z M62 40 L55 54 H69 Z"/>
        </g>
      </svg>
    </div>
    <p class="feature-label">MY COURT<br>DATES</p>
  </section>

  <section class="feature feature--payments">
    <div class="feature-badge">
      <svg width="90" height="56" viewBox="0 0 90 56" fill="none" stroke="#fff" stroke-width="4">
        <rect x="4" y="4" width="82" height="48" rx="2"/>
        <path d="M18 16 C12 22 12 34 18 40 M72 16 C78 22 78 34 72 40"/>
        <circle cx="45" cy="28" r="13"/>
        <text x="45" y="35" text-anchor="middle" fill="#fff" stroke="none" font-family="Noto Sans, sans-serif" font-weight="700" font-size="20">$</text>
      </svg>
    </div>
    <p class="feature-label">MY PAYMENTS</p>
  </section>

  <div class="brand-seal">
    <p class="brand-name">Brightwell<br>Docket</p>
  </div>

  <p class="and-more">... AND MORE!</p>

  <p class="cta">CONTACT ME TODAY</p>

  <p class="agent-name">DANA<br>MORROW</p>

  <div class="contact contact--email">
    <p class="contact-label">EMAIL</p>
    <p class="contact-value">DANA@bwd.example</p>
  </div>

  <div class="contact contact--phone">
    <p class="contact-label">TEXT OR PHONE</p>
    <p class="contact-value">555-014-0199</p>
  </div>
</main>
</body>
</html>
```